Steel Company / Iron Railing Business Card Template

We are a custom steel fabrication company located in Ashby Mills, PA. In business since 1979, we recently developed a new logo, and we're looking for a business card design to help display the new logo and our business. The name of the company is Kelbrook Forge Co.. The Office Phone number is (610) 555-0143. We fabricate and install custom "wrought iron" railings on our residential side, we also fabricate and erect structural steel (think cranes and steel beams in buildings) on our commercial side. Looking to get a business card template designed. Something modern, but professional. Clear and easy to read. Front should have all business and employee information including phone number(s), email address, business information, etc. back should spotlight logo.

Industry/Entity Type

Construction / Home Improvement

Contact Information for Business Card

Business information is Kelbrook Forge Co., 48 Dunmore Ave Suite 3305, Ashby Mills, PA 19074. Phone number is (610) 555-0143. Website is www.kelbrookforge.example Business card should be for "Tom Pelling" with the job title "Sales & Estimating" but be editable for other employees. Tom's phone number is (610) 555-0178

Colors

Designer to choose colors to be used in the design.

Requirements
Must have
• Modern Feel, Design should be sized for standard business card sizing 3.5" x 2" (88.9mm x 50.8mm)

```html
<!DOCTYPE html>
<html lang="en">
<head>
<meta charset="utf-8">
<title>Kelbrook Forge Co. — Business Card</title>
<link href="https://fonts.googleapis.com/css2?family=Lato:wght@400;700;900&display=swap" rel="stylesheet">
<style>
  :root {
    --navy: #23418f;
    --red: #d9352f;
    --ink: #2b2b2b;
    --paper: #ffffff;
    --backdrop: #e6e7ea;
  }
  * { margin: 0; padding: 0; box-sizing: border-box; }
  html, body { width: 1200px; height: 915px; overflow: hidden; }
  body {
    background: var(--backdrop);
    font-family: "Lato", sans-serif;
    position: relative;
  }
  .card {
    position: absolute;
    width: 560px;
    height: 320px;
    background: var(--paper);
    border-radius: 18px;
    overflow: hidden;
    box-shadow: 0 10px 30px rgba(0,0,0,0.18);
  }
  .card--back { left: 60px; top: 90px; }
  .card--front { left: 580px; top: 505px; }

  .brand {
    position: absolute;
    display: flex;
    align-items: center;
    gap: 12px;
    color: var(--navy);
    font-weight: 900;
    white-space: nowrap;
  }
  .brand__dot {
    width: 22px; height: 22px;
    border-radius: 50%;
    background: var(--red);
    flex: none;
  }
  .card--back .brand {
    left: 50%; top: 50%;
    transform: translate(-50%, -50%);
    font-size: 38px;
  }
  .card--front .brand {
    left: 32px; top: 150px;
    font-size: 25px;
    gap: 10px;
  }
  .card--front .brand__dot { width: 15px; height: 15px; }

  .divider {
    position: absolute;
    left: 318px; top: 96px;
    width: 2px; height: 150px;
    background: var(--navy);
  }
  .contact {
    position: absolute;
    left: 334px; top: 26px;
    width: 220px;
    color: var(--ink);
    font-size: 13px;
    line-height: 1.4;
  }
  .contact__name {
    color: var(--navy);
    font-size: 25px;
    font-weight: 700;
    line-height: 1.1;
  }
  .contact__title { font-size: 14px; margin-bottom: 6px; }
  .contact__company { color: var(--navy); font-weight: 700; font-size: 14px; }
  .contact__lines { list-style: none; margin-top: 6px; }
  .contact__lines li { display: flex; align-items: center; gap: 7px; }
  .contact__lines svg { width: 12px; height: 12px; fill: var(--navy); flex: none; }

  .band { position: absolute; left: 0; bottom: 0; width: 560px; height: 90px; }
  .website {
    position: absolute;
    right: 22px; bottom: 22px;
    color: var(--paper);
    font-size: 13px;
    letter-spacing: 0.3px;
  }
</style>
</head>
<body>

  <section class="card card--back" aria-label="Card back">
    <div class="brand"><span class="brand__dot"></span>Kelbrook Forge Co.</div>
  </section>

  <section class="card card--front" aria-label="Card front">
    <div class="brand"><span class="brand__dot"></span>Kelbrook Forge Co.</div>

    <div class="divider"></div>

    <div class="contact">
      <p class="contact__name">Tom Pelling</p>
      <p class="contact__title">Sales &amp; Estimating</p>
      <p class="contact__company">Kelbrook Forge Co.,</p>
      <p>48 Dunmore Ave Suite 3305,<br>Ashby Mills, PA 19074</p>
      <ul class="contact__lines">
        <li><svg viewBox="0 0 24 24"><path d="M6.6 10.8a15 15 0 0 0 6.6 6.6l2.2-2.2c.3-.3.7-.4 1-.2 1.1.4 2.3.6 3.6.6.6 0 1 .4 1 1V20c0 .6-.4 1-1 1A17 17 0 0 1 3 4c0-.6.4-1 1-1h3.5c.6 0 1 .4 1 1 0 1.3.2 2.5.6 3.6.1.3 0 .7-.2 1z"/></svg>(610) 555-0143</li>
        <li><svg viewBox="0 0 24 24"><path d="M7 1h10a2 2 0 0 1 2 2v18a2 2 0 0 1-2 2H7a2 2 0 0 1-2-2V3a2 2 0 0 1 2-2zm0 3v15h10V4zm5 16.2a1 1 0 1 0 0 .1z"/></svg>(610) 555-0178</li>
        <li><svg viewBox="0 0 24 24"><path d="M2 5h20v14H2zm2 2v.5l8 5 8-5V7zm0 2.8V17h16V9.8l-8 5z"/></svg>info@kelbrookforge.example</li>
      </ul>
    </div>

    <svg class="band" viewBox="0 0 560 90" preserveAspectRatio="none" aria-hidden="true">
      <path d="M0 70 L330 26" stroke="var(--red)" stroke-width="5" fill="none"/>
      <path d="M0 90 L0 80 L340 36 C356 34 362 22 380 22 L560 22 L560 90 Z" fill="var(--navy)"/>
    </svg>
    <p class="website">www.kelbrookforge.example</p>
  </section>

</body>
</html>
```